Kernwichtel sucht neue Visitenkarten & Briefpapier
Zielgruppe
Wir sind ein Start-Up das unter kernwichtel-beispiel.de ab 2014, deutschlandweit gesunde und frische Früchte zu Ihnen nach Hause oder an den Arbeitsplatz als Abo (wöchentlich/monatlich) per Post liefern möchte. Es sollten später auch Filialen in Deutschland eröffnet werden.
Aufgabenstellung
Entwicklung einer ansprechenden Visitenkarte und Briefpapier. Gestalterische Basis hierfür ist unser Logo. Das Logo kann gerade, oder gedreht werden. Das Briefpapier dient als Rechnung/Lieferschein und Korrespondenz unserer Firma. Das Briefpapier ist 1-Seitig. Die Visitenkarte ist ebenfalls 1-Seitig und auf Deutsch.
Das Design soll "das gewisse Etwas haben" und nicht zu verspielt sein.

```html
<!DOCTYPE html>
<html lang="de">
<head>
<meta charset="utf-8">
<title>Kernwichtel – Briefpapier &amp; Visitenkarten</title>
<link rel="stylesheet" href="https://fonts.googleapis.com/css2?family=Arimo:wght@400;700&family=Source+Sans+3:wght@400;600&display=swap">
<style>
:root{
  --green:#8bc043;
  --green-deep:#6fb21c;
  --yellow:#fdc600;
  --ink:#111;
  --paper:#fff;
  --bg:#b9b9b9;
  --ink-blue:#1a1adf;
}
*{margin:0;padding:0;box-sizing:border-box}
html,body{width:1200px;height:1115px;overflow:hidden}
body{background:radial-gradient(ellipse at 90% 40%,#f0f0f0 0%,var(--bg) 60%,#a9a9a9 100%);position:relative;font-family:"Arimo",Arial,sans-serif;color:var(--ink)}
.letter{position:absolute;left:14px;top:21px;width:770px;height:1073px;background:var(--paper);box-shadow:0 4px 14px rgba(0,0,0,.45);overflow:hidden}
.letter__band{position:absolute;left:0;width:100%}
.band--green-top{top:0;height:53px;background:var(--green)}
.band--yellow-top{top:53px;height:17px;background:var(--yellow);box-shadow:0 3px 5px rgba(0,0,0,.2)}
.band--yellow-foot{top:876px;height:12px;background:var(--yellow)}
.letter__footer{position:absolute;left:0;top:888px;width:100%;height:185px;background:var(--green);color:#fff;font-family:"Source Sans 3",sans-serif}
.brand{position:absolute;display:flex;align-items:center;gap:8px;font-family:"Arimo",Arial,sans-serif;font-weight:700}
.brand__dot{border-radius:50%;background:var(--yellow);flex:none}
.letter .brand{left:500px;top:185px;font-size:34px;color:#5f9e1f}
.letter .brand__dot{width:34px;height:34px}
.sender-line{position:absolute;left:52px;top:134px;font-size:8px;padding-bottom:2px;border-bottom:1px solid var(--yellow)}
.recipient{position:absolute;left:52px;top:158px;font-size:13px;line-height:16.5px}
.recipient strong{font-weight:700}
.fold-mark{position:absolute;left:0;width:12px;border-top:1px solid #666}
.subject{position:absolute;left:52px;top:301px;font-size:13.5px;font-weight:700}
.salutation{position:absolute;left:53px;top:355px;font-size:13.5px;font-weight:700}
.date{position:absolute;right:53px;top:355px;font-size:13.5px}
.body-text{position:absolute;left:53px;top:392px;width:664px;font-size:13.4px;line-height:17.8px;letter-spacing:-.35px;text-align:justify}
.body-text p{margin-bottom:17.8px}
.closing{position:absolute;left:53px;top:793px;font-size:13.5px}
.signature{position:absolute;left:53px;top:811px;width:185px;height:30px;background:linear-gradient(90deg,rgba(26,26,223,.15),rgba(26,26,223,.3))}
.signer{position:absolute;left:53px;top:843px;font-size:13.5px}
.foot-name{position:absolute;right:570px;top:24px;text-align:right;line-height:1}
.foot-name .company{font-size:22px}
.foot-name .person{font-size:14px;font-weight:600;display:block;margin-top:2px}
.foot-address{position:absolute;right:570px;top:92px;text-align:right;font-size:14px;line-height:16px}
.foot-contact{position:absolute;right:317px;top:43px;text-align:right;font-size:11px;line-height:13px}
.foot-web{position:absolute;right:317px;top:95px;text-align:right;font-size:11px;line-height:13px}
.foot-bank{position:absolute;right:53px;top:43px;text-align:right;font-size:11px;line-height:15px}
.card{position:absolute;left:821px;width:345px;height:232px;background:radial-gradient(ellipse at 40% 60%,#94c653 0%,var(--green-deep) 90%);box-shadow:0 4px 12px rgba(0,0,0,.4);color:#fff;font-family:"Source Sans 3",sans-serif}
.card--front{top:237px}
.card--back{top:652px}
.card--front .brand{left:0;right:0;top:96px;justify-content:center;font-size:34px;color:#fff}
.card--front .brand__dot{width:30px;height:30px;background:#fff}
.card--back .brand{left:10px;top:98px;font-size:20px;color:#fff}
.card--back .brand__dot{width:22px;height:22px}
.card__title{position:absolute;right:36px;top:16px;font-size:19px;font-weight:600}
.card__block{position:absolute;right:36px;text-align:right;font-size:11px;line-height:13px}
.card__person{position:absolute;right:226px;top:194px;text-align:right;font-size:11px;line-height:12px}
.card__person strong{font-weight:600}
</style>
</head>
<body>
<section class="letter" aria-label="Briefpapier">
  <div class="letter__band band--green-top"></div>
  <div class="letter__band band--yellow-top"></div>
  <div class="brand"><span class="brand__dot"></span>Kernwichtel</div>
  <p class="sender-line">Kernwichtel AG | Lindenauer Weg 7 | D-04229 Leipzig</p>
  <address class="recipient" style="font-style:normal">
    <strong>Musterfirma GmbH</strong><br>Herr Mustermann<br>Musterstraße 21<br><br>D-012345 Musterstadt
  </address>
  <span class="fold-mark" style="top:288px"></span>
  <span class="fold-mark" style="top:724px"></span>
  <p class="subject">Betreff: Hier können Sie ihren Betreff einfügen</p>
  <p class="salutation">Sehr geehrter Herr Mustermann,</p>
  <p class="date">Leipzig, den 01.01.2014</p>
  <div class="body-text">
    <p>Gepfiffen gegenteil er es zufrieden mannsbild ertastete he. Mi zopfen freund frauen du herein. Gefegt vor lassen marder andrer ihr hangen kleine. So aufzulosen dammerigen nachmittag ja ku du. Aneinander um du lattenzaun ob bodenlosen kartoffeln la. He vogelnest pa gestorben zu filzhutes zuschauen ja.</p>
    <p>Die weiterhin verweilen einfacher duftenden bei geh musterung. Einfach fremder uhr gefreut saubere gru antwort ten die. Als weiblein lampchen schlafer burschen das wohlfeil gut art. Fast kaum tut aber auch hoch nie dort. Gerochen ihr schlafet tat ein gerberei wunschte ehe vollbart blattern. Wieder ri um gelang feinen keinem in bi. Ebenso he ja lebtag vorbei da. Halboffene da achthausen vorsichtig bi du gerbersteg. Schaute klopfte zwingen gelernt mit unrecht auffiel bei. See verlohnt getraumt wer begegnen sto spateren sorgfalt. Te im sondern schritt gelernt sa wahrend meisten fenster so. Sieben kugeln da worden mi wo. Eisen gut viele tun sagte guten. Es sa he zu wirrwarr schmales burschen. Lauschte leuchter ob trillern am. Gefallts du arbeiter uberlegt ri frohlich.</p>
    <p>Mannsbild mitkommen ist unendlich schwarzes und wie schlupfte vor. Werdet bat das gut dunner lebtag der allein. Zum sorglosen gib tut wohnstube muhlenrad beneidest. Damit zahne da keine ubers te abend. Mann an je gelt kein fest hast. Madchens schaffte an stabelle heiraten um. Ja stickig konntet richtig du zu ubrigen gewohnt ei.</p>
    <p>Es rausperte grasplatz neugierde ku sa weiterhin naturlich schwachem. Unten dahin ein getan sitte genug habet nur vor hei. Sonst von ihren kuche kunde lauft seine ihr weg. Drohte te langen kennen em um. Weg sahen mager tiefe sie gut wei. Vogelnest das bewirtung bat wachsamen bis vergnugen. Recht im am kinde ganze da einer wesen er.</p>
  </div>
  <p class="closing">Mit freundlichen Grüßen</p>
  <div class="signature" role="img" aria-label="Handschriftliche Unterschrift in blauer Tinte"></div>
  <p class="signer">Jonas Feldberg</p>
  <div class="letter__band band--yellow-foot"></div>
  <footer class="letter__footer">
    <div class="foot-name"><span class="company">Kernwichtel AD</span><span class="person">Jonas Feldberg</span></div>
    <p class="foot-address">Lindenauer Weg 7<br>D-04229 Leipzig</p>
    <p class="foot-contact">Tel.: 0341 55501234<br>Fax.: 0341 55501239</p>
    <p class="foot-web">jfeldberg@kernwichtel-beispiel.de<br>www.kernwichtel-beispiel.de</p>
    <p class="foot-bank">Musterbank<br>IBAN: DE97 1234 0000 1000 0000 00<br>BIC: XXXXXXX<br>Steur-Nr.: 100 / 100 / 10000</p>
  </footer>
</section>

<section class="card card--front" aria-label="Visitenkarte Vorderseite">
  <div class="brand"><span class="brand__dot"></span>Kernwichtel</div>
</section>

<section class="card card--back" aria-label="Visitenkarte Rückseite">
  <p class="card__title">Kernwichtel AG</p>
  <div class="brand"><span class="brand__dot"></span>Kernwichtel</div>
  <p class="card__block" style="top:78px">Lindenauer Weg 7<br>D-04229 Leipzig</p>
  <p class="card__block" style="top:134px">Tel.: 0341 55501234<br>Fax.: 0341 55501239</p>
  <p class="card__block" style="top:188px">jfeldberg@kernwichtel-beispiel.de<br>www.kernwichtel-beispiel.de</p>
  <p class="card__person"><strong>Jonas Feldberg</strong><br>CEO &amp; Founder</p>
</section>
</body>
</html>
```